Medical equipment business looking for professional, unique business card

We need a business card design for a durable medical equipment company. We are small but would like our cards to express that we are much bigger. We focus on braces (back, knee, wrist, etc) but also do crutches, rollators, wheelchairs- basically medical equipment that gets you going and back in Action. Our colors are blue and green and our logo has an arrow and use of a "spine". We'd like to express professionalism while being unique.

Industry/Entity Type

Medical Equipment

Contact Information for Business Card

Professional feel but unique. Memorable.

Font styles to use
Serif
Sans Serif
Other font styles liked:
• verdana

Requirements
Must have
• card holders cell#, business phone#, fax#, email, website address, business address, logo
Nice to have
• use of medical/healthcare related descriptive words, items, look
Should not have
• the wrong colors or cartoon characters.

```html
<!DOCTYPE html>
<html lang="en">
<head>
<meta charset="utf-8">
<title>Strideway Business Card</title>
<link rel="stylesheet" href="https://fonts.googleapis.com/css2?family=Noto+Sans:wght@400;700&display=swap">
<style>
  :root {
    --backdrop: #5b4a3b;
    --navy: #00426a;
    --lime: #8dc63f;
    --white: #ffffff;
    --ink: #0d466b;
    --card-shadow: 0 3px 8px rgba(0,0,0,.35);
  }
  html, body {
    margin: 0;
    width: 1200px;
    height: 987px;
    overflow: hidden;
    background: var(--backdrop);
    font-family: "Noto Sans", Verdana, sans-serif;
  }
  .card {
    position: absolute;
    width: 615px;
    height: 352px;
    border-radius: 21px;
    overflow: hidden;
    box-shadow: var(--card-shadow);
  }
  .card--front { left: 293px; top: 130px; background: var(--white); }
  .card--back { left: 292px; top: 505px; background: var(--lime); }

  .front-panel { position: absolute; inset: 0; }

  .contact {
    position: absolute;
    left: 29px;
    top: 62px;
    color: var(--white);
  }
  .contact__name {
    margin: 0;
    font-size: 23px;
    font-weight: 700;
    color: var(--lime);
    letter-spacing: .3px;
  }
  .contact__title {
    margin: 4px 0 0;
    font-size: 17.5px;
  }
  .contact__address {
    margin: 12px 0 0;
    font-size: 16px;
    line-height: 20px;
    font-style: normal;
  }
  .contact__list {
    list-style: none;
    margin: 13px 0 0;
    padding: 0;
    font-size: 16px;
  }
  .contact__list li {
    display: flex;
    align-items: center;
    height: 23.4px;
  }
  .contact__icon {
    width: 16px;
    height: 16px;
    margin-right: 9px;
    fill: var(--lime);
    flex: none;
  }

  .brand {
    position: absolute;
    display: flex;
    align-items: center;
    gap: 10px;
    color: var(--ink);
    font-weight: 700;
    white-space: nowrap;
  }
  .brand__dot {
    border-radius: 50%;
    background: var(--lime);
  }
  .card--front .brand { left: 328px; top: 160px; font-size: 38px; }
  .card--front .brand__dot { width: 14px; height: 14px; }
  .card--back .brand { left: 50%; top: 50%; transform: translate(-50%, -58%); font-size: 46px; }
  .card--back .brand__dot { width: 16px; height: 16px; background: var(--ink); }
</style>
</head>
<body>

<section class="card card--front">
  <svg class="front-panel" viewBox="0 0 615 352" width="615" height="352">
    <path d="M0,0 H340 C284,100 284,250 346,352 H0 Z" fill="var(--lime)"/>
    <path d="M0,0 H331 C272,95 272,250 323,352 H0 Z" fill="var(--navy)"/>
    <path d="M331,0 C272,95 272,250 323,352" fill="none" stroke="var(--white)" stroke-width="2"/>
  </svg>

  <div class="contact">
    <h1 class="contact__name">Dana Whitfield</h1>
    <p class="contact__title">CEO/Founder</p>
    <address class="contact__address">412 Birchwood Road<br>Fairview, Oregon 97024</address>
    <ul class="contact__list">
      <li><svg class="contact__icon" viewBox="0 0 16 16"><path d="M3.6 1.2l2.3 2.6-1.3 2a9 9 0 0 0 5.6 5.6l2-1.3 2.6 2.3-1.4 2.3C7.6 16.3-.3 8.4 1.3 2.6z"/></svg>555 214 7730</li>
      <li><svg class="contact__icon" viewBox="0 0 16 16"><path d="M4.5 0h7A1.5 1.5 0 0 1 13 1.5v13a1.5 1.5 0 0 1-1.5 1.5h-7A1.5 1.5 0 0 1 3 14.5v-13A1.5 1.5 0 0 1 4.5 0zM5 2v10h6V2zm3 11a1 1 0 1 0 0 2 1 1 0 0 0 0-2z"/></svg>555 386 1492</li>
      <li><svg class="contact__icon" viewBox="0 0 16 16"><path d="M4 1h6l2 2v3H4zM1 7h14v7H1zm2 2v1h4V9zm0 2v1h4v-1zm7-2v1h3V9z"/></svg>555 902 6518</li>
      <li><svg class="contact__icon" viewBox="0 0 16 16"><path d="M1 3h14v1L8 9 1 4zm0 2.5l7 5 7-5V13H1z"/></svg>name@strideway.com</li>
      <li><svg class="contact__icon" viewBox="0 0 16 16"><circle cx="8" cy="8" r="7"/><path d="M4 5c2 0 2 2 4 2s1 3-1 3-1 3-2 4M10 2c0 2 2 2 3 3" fill="none" stroke="var(--navy)" stroke-width="1.3"/></svg>www.strideway.com</li>
    </ul>
  </div>

  <div class="brand"><span class="brand__dot"></span>Strideway</div>
</section>

<section class="card card--back">
  <div class="brand"><span class="brand__dot"></span>Strideway</div>
</section>

</body>
</html>
```